Criação de Papelaria Profissional para Decoração & Mobília
" Loja online, com objetivo de abrir a loja física com objetivo de entregar produtos diferenciados "

```html
<!DOCTYPE html>
<html lang="pt-BR">
<head>
<meta charset="utf-8">
<title>Altivara — Cartão de Visita</title>
<link href="https://fonts.googleapis.com/css2?family=Montserrat:wght@300;400;500&display=swap" rel="stylesheet">
<style>
  :root {
    --backdrop: #e4e4e2;
    --navy: #1d2850;
    --gold: #c29a5b;
    --paper: #ffffff;
    --ink: #4a4a4a;
    --ink-soft: #8a8a8a;
    --pattern: #dcdde2;
  }
  * { margin: 0; padding: 0; box-sizing: border-box; }
  html, body { width: 1200px; height: 1200px; overflow: hidden; }
  body {
    background: var(--backdrop);
    font-family: "Montserrat", sans-serif;
    display: flex;
    flex-direction: column;
    align-items: center;
    justify-content: center;
    gap: 60px;
  }
  .card {
    width: 800px;
    height: 444px;
    position: relative;
    overflow: hidden;
    box-shadow: 0 6px 18px rgba(0,0,0,0.12);
  }

  /* Front */
  .card--front { background: var(--navy); }
  .brand-name {
    font-family: "Montserrat", sans-serif;
    font-weight: 400;
    color: var(--gold);
    letter-spacing: 0.42em;
    text-transform: uppercase;
  }
  .card--front .brand-name {
    position: absolute;
    top: 170px;
    left: 0; right: 0;
    text-align: center;
    font-size: 46px;
    padding-left: 0.42em;
  }
  .web-row {
    position: absolute;
    top: 300px;
    left: 0; right: 0;
    display: flex;
    align-items: center;
    gap: 26px;
  }
  .web-row .rule { flex: 1; height: 2px; background: var(--gold); }
  .web-row .rule--left { margin-left: 240px; }
  .web-row .rule--right { margin-right: 0; }
  .website {
    color: #ffffff;
    font-size: 15px;
    font-weight: 300;
    letter-spacing: 0.4em;
  }

  /* Back */
  .card--back { background: var(--paper); }
  .pattern-field {
    position: absolute;
    top: 0; right: 0;
    width: 480px; height: 444px;
    background: radial-gradient(ellipse at 70% 35%, var(--pattern) 0%, rgba(220,221,226,0.5) 40%, rgba(255,255,255,0) 75%);
  }
  .contact {
    position: absolute;
    top: 60px;
    left: 48px;
  }
  .person { display: flex; align-items: flex-start; gap: 12px; margin-bottom: 30px; }
  .person .mark { width: 22px; height: 22px; background: var(--gold); margin-top: 2px; }
  .person-name {
    color: var(--gold);
    font-size: 19px;
    font-weight: 500;
    letter-spacing: 0.04em;
    text-transform: uppercase;
  }
  .person-role { color: var(--ink-soft); font-size: 14px; margin-top: 4px; }
  .contact-list { list-style: none; }
  .contact-list li {
    display: flex;
    align-items: flex-start;
    gap: 12px;
    color: var(--ink);
    font-size: 14px;
    line-height: 1.35;
    margin-bottom: 11px;
  }
  .contact-list svg { width: 18px; height: 18px; flex: none; margin-top: 1px; }
  .card--back .brand-name {
    position: absolute;
    top: 250px;
    left: 430px;
    font-size: 38px;
  }
</style>
</head>
<body>

  <section class="card card--front" aria-label="Frente do cartão">
    <div class="brand-name">Altivara</div>
    <div class="web-row">
      <span class="rule rule--left"></span>
      <span class="website">www.altivara.com.br</span>
      <span class="rule rule--right"></span>
    </div>
  </section>

  <section class="card card--back" aria-label="Verso do cartão">
    <div class="pattern-field" role="img" aria-label="Padrão decorativo de pontos em cinza claro"></div>

    <div class="contact">
      <div class="person">
        <span class="mark"></span>
        <div>
          <div class="person-name">Lucas Andrade</div>
          <div class="person-role">Diretora</div>
        </div>
      </div>
      <ul class="contact-list">
        <li>
          <svg viewBox="0 0 18 18"><circle cx="9" cy="9" r="9" fill="#c29a5b"/><path d="M6 4.5c.6 0 1.2 1.6 1.2 2 0 .5-.7.7-.6 1.1.3.9 1.4 2 2.3 2.3.4.1.6-.6 1.1-.6.4 0 2 .6 2 1.2 0 .8-1 1.6-1.8 1.5C8 11.8 6.2 10 5.3 7.8 5 6.8 5.4 4.5 6 4.5z" fill="#fff"/></svg>
          <span>11 3210-4587</span>
        </li>
        <li>
          <svg viewBox="0 0 18 18"><circle cx="9" cy="9" r="9" fill="#c29a5b"/><rect x="4.5" y="6" width="9" height="6.5" rx="0.8" fill="none" stroke="#fff" stroke-width="1.2"/><path d="M4.8 6.4 9 9.6l4.2-3.2" fill="none" stroke="#fff" stroke-width="1.2"/></svg>
          <span>contato@altivara.com.br</span>
        </li>
        <li>
          <svg viewBox="0 0 18 18"><circle cx="9" cy="9" r="9" fill="#c29a5b"/></svg>
          <span>@altivara</span>
        </li>
        <li>
          <svg viewBox="0 0 18 18"><circle cx="9" cy="9" r="9" fill="#c29a5b"/><path d="M9 3.8a3.4 3.4 0 0 0-3.4 3.4c0 2.5 3.4 6.5 3.4 6.5s3.4-4 3.4-6.5A3.4 3.4 0 0 0 9 3.8z" fill="#fff"/><circle cx="9" cy="7.2" r="1.2" fill="#c29a5b"/></svg>
          <span>Av. das Palmeiras, 512<br>São Paulo - SP</span>
        </li>
      </ul>
    </div>

    <div class="brand-name">Altivara</div>
  </section>

</body>
</html>
```